A new fresh and flat K&T Logistics Brochure Design A4 - 4 pages

Our client is an established International Logistics firm looking to upgrade their sales brochure.
We would like the designer to create concepts that are flat, modern and communicate reliability and expediency to our clients. We want the brochure to maintain a degree of white space and minimal design.
Introduction
LOGISTICS - it's what we do best! We're proud to say so after 27 years (and counting) of organic growth within the 3PL industry. Starting off in Meridian, Mississippi with a fleet of 4 trucks in 1987, K&T is today a global 3PL company with offices in the United States and Asia Pacific region.
Our goal has always been to serve our clients by getting things done, and getting them done right.
Format: A4 4-sided brochure
Pg 1 Front Page - Company name and logo, and vector design concept to make front page unique. Please try to include some kind of container reference design on the front page (e.g 2D or 3D vector, transparent overlay etc...), place this design element somewhere in the middle or bttom of the page.
Pg 2 and/or Pg 3
- Introduction and Core services Including: ABOUT, SERVICES, CONTRACT LOGISTICS, K&T INTEL (following the menu content of our website www.ktvrx.example)
- Text space to explain Services in more detail.
Social proof (existing client testimonials/feedback.)
- A 'C.A.R.E' acronym design element, including the words: Communicative, Accessible, Responsible, Efficient
Pg 4 Back Page- Contact information, Call to action.
Throughut the brochure please leave space for images as you deem appropriate and we will update late OR even better usesome of your own stock images.
Color theme: Based on corporate colors (but not limited to), see website
http://www.ktvrx.example
Try diffent font types to the website both serif and sans serif
Include several CTAs throughout the brochure.
You can use both the attached pdf brochure and the website for content.
We would also appreciate if you could also enhance the logo to make it 'pop' (keep shape and style).

```html
<!DOCTYPE html>
<html lang="en">
<head>
<meta charset="utf-8">
<title>K&amp;T Logistics – Brochure Back and Front</title>
<link rel="stylesheet" href="https://fonts.googleapis.com/css2?family=Open+Sans:ital,wght@0,300;0,400;0,600;0,700;1,400;1,600&display=swap">
<style>
  :root{
    --stage:#dfe8ef;
    --white:#ffffff;
    --orange:#f7860f;
    --orange-dark:#e06f00;
    --brand-blue:#4a7fb0;
    --steel-blue:#5a89b8;
    --pale-blue:#e4eef6;
    --mist-blue:#c9dcec;
    --deep-blue:#3c6d9d;
    --ink:#1e1e1e;
    --grey:#7d8b96;
  }
  *{box-sizing:border-box;margin:0;padding:0}
  html,body{width:1200px;height:856px;overflow:hidden}
  body{background:var(--stage);font-family:"Open Sans",Arial,sans-serif;position:relative}

  .spread{position:absolute;left:160px;top:90px;width:880px;height:640px;display:flex;box-shadow:0 8px 24px rgba(40,70,100,.18)}
  .panel{position:relative;width:440px;height:640px;overflow:hidden;background:var(--white)}

  /* ---------- back panel ---------- */
  .contact-head{position:absolute;left:0;top:0;width:100%;height:88px;padding:6px 18px}
  .contact-title{font-size:34px;font-weight:400;color:var(--orange);line-height:1.2}
  .contact-company{font-size:24px;color:var(--ink);line-height:1.1}
  .contact-company .accent{color:var(--brand-blue)}
  .contact-zone{position:absolute;left:0;top:88px;width:100%;height:252px;background:var(--pale-blue)}
  .region-map{position:absolute;left:10px;top:18px;width:200px;height:158px}
  .phone-list{position:absolute;left:225px;top:88px;z-index:1;list-style:none;font-size:14px;color:var(--steel-blue);line-height:25px;white-space:nowrap}
  .phone-list b{font-weight:400;color:var(--ink)}
  .call-button{position:absolute;left:224px;top:164px;width:190px;height:36px;border-radius:3px;
    background:linear-gradient(var(--orange),var(--orange-dark));color:var(--white);font-weight:700;
    font-size:21px;text-align:center;line-height:36px;box-shadow:0 1px 2px rgba(0,0,0,.25)}
  .photo-grid{position:absolute;left:0;top:340px;width:100%;height:238px;display:grid;
    grid-template-columns:repeat(5,1fr);grid-template-rows:1fr 1fr;gap:4px;background:var(--white)}
  .photo-tile{background:linear-gradient(160deg,#8fb0d2,#4f7fae 70%,#6f97c0)}
  .contact-foot{position:absolute;left:0;bottom:0;width:100%;height:62px;background:var(--steel-blue);
    color:var(--white);font-size:13px;padding:0 16px;display:flex;align-items:center;justify-content:space-between}
  .contact-foot .label{font-weight:700}
  .social{display:flex;align-items:center;gap:8px}
  .social-item{display:flex;align-items:center;gap:3px;font-size:12px}
  .social-item::before{content:"";width:10px;height:10px;background:var(--white)}

  /* ---------- front panel ---------- */
  .front-art{position:absolute;inset:0}
  .brand{position:absolute;left:14px;top:14px;display:flex;align-items:center;gap:8px}
  .brand-mark{width:18px;height:18px;background:var(--brand-blue)}
  .brand-name{font-size:40px;font-weight:700;color:var(--brand-blue);line-height:1}
  .brand-tagline{position:absolute;right:26px;top:54px;font-size:14px;font-style:italic;font-weight:600;color:var(--deep-blue)}
  .headline{position:absolute;right:26px;top:100px;text-align:right;font-size:32px;font-weight:400;color:var(--ink);line-height:1.1;white-space:nowrap}
  .headline .air{color:var(--brand-blue)}
  .headline .sea{color:var(--orange)}
  .headline-sub{position:absolute;right:28px;top:140px;font-size:22px;color:var(--grey)}
  .services{position:absolute;left:24px;top:482px;color:var(--white)}
  .services-title{font-size:40px;font-weight:400;line-height:1;color:var(--white)}
  .services-title span{font-size:22px;color:var(--ink)}
  .services-list{list-style:none;font-size:13px;line-height:18px;margin-top:6px}
  .services-list li{display:flex;align-items:flex-start;gap:8px}
  .services-list svg{margin-top:4px;flex:none}
</style>
</head>
<body>
<main class="spread">

  <section class="panel panel-back">
    <header class="contact-head">
      <h1 class="contact-title">Contact Information</h1>
      <p class="contact-company"><span class="accent">K&amp;T</span> Logistics</p>
    </header>

    <div class="contact-zone">
      <svg class="region-map" viewBox="0 0 200 158" role="img" aria-label="Map of the Central Asian region served">
        <defs>
          <linearGradient id="mapTone" x1="0" y1="0" x2="1" y2="1">
            <stop offset="0" stop-color="#5a89b8"/><stop offset="1" stop-color="#4a7fb0"/>
          </linearGradient>
        </defs>
        <rect width="200" height="158" rx="6" fill="url(#mapTone)"/>
      </svg>
      <ul class="phone-list">
        <li>+1 <b>(555)</b> 014 2290 (US)</li>
        <li>+86 <b>(555)</b> 0100 4417 (Asia)</li>
        <li>+852 5550 1846 (HK)</li>
      </ul>
      <div class="call-button">Call NOW</div>
    </div>

    <div class="photo-grid" role="img" aria-label="Blue-toned photos of a container port, cranes, a cargo ship and trucks on a highway">
      <div class="photo-tile"></div><div class="photo-tile"></div><div class="photo-tile"></div><div class="photo-tile"></div><div class="photo-tile"></div>
      <div class="photo-tile"></div><div class="photo-tile"></div><div class="photo-tile"></div><div class="photo-tile"></div><div class="photo-tile"></div>
    </div>

    <footer class="contact-foot">
      <p><span class="label">Email:</span> info@ktfreight.example</p>
      <div class="social">
        <span>Find us</span>
        <span class="social-item">Chatter</span>
        <span class="social-item">Linkup</span>
      </div>
    </footer>
  </section>

  <section class="panel panel-front">
    <svg class="front-art" viewBox="0 0 440 640" preserveAspectRatio="none">
      <defs>
        <linearGradient id="skyTone" x1="0" y1="0" x2="1" y2="1">
          <stop offset="0" stop-color="#c9dcec"/><stop offset=".55" stop-color="#e9f1f8"/><stop offset="1" stop-color="#8fb2d2"/>
        </linearGradient>
      </defs>
      <polygon points="0,95 440,345 440,565 368,530 0,500" fill="url(#skyTone)" role="img"
        aria-label="Illustration of a city skyline with a plane, a truck, a container ship and a high-speed train"/>
      <polygon points="0,370 100,430 0,505" fill="var(--deep-blue)"/>
      <polygon points="0,505 165,430 368,530 128,645 0,645" fill="var(--orange)"/>
    </svg>

    <div class="brand"><span class="brand-mark"></span><span class="brand-name">K&amp;T</span></div>
    <p class="brand-tagline">Logistics and Supply Chain Solutions</p>
    <h2 class="headline">LAND, <span class="air">AIR OR</span> <span class="sea">SEA??</span></h2>
    <p class="headline-sub">......Get easy</p>

    <div class="services">
      <h3 class="services-title">CORE <span>SERVICES</span></h3>
      <ul class="services-list">
        <li><svg width="11" height="10" viewBox="0 0 11 10"><path d="M1 5l3 3 6-7" fill="none" stroke="#1e1e1e" stroke-width="2"/></svg>Sea Transportation</li>
        <li><svg width="11" height="10" viewBox="0 0 11 10"><path d="M1 5l3 3 6-7" fill="none" stroke="#1e1e1e" stroke-width="2"/></svg>Air Transportation</li>
        <li><svg width="11" height="10" viewBox="0 0 11 10"><path d="M1 5l3 3 6-7" fill="none" stroke="#1e1e1e" stroke-width="2"/></svg>Road Transportation</li>
        <li><svg width="11" height="10" viewBox="0 0 11 10"><path d="M1 5l3 3 6-7" fill="none" stroke="#1e1e1e" stroke-width="2"/></svg>Warehousing &amp;</li>
        <li><svg width="11" height="10" viewBox="0 0 11 10"><path d="M1 5l3 3 6-7" fill="none" stroke="#1e1e1e" stroke-width="2"/></svg>Distribution</li>
      </ul>
    </div>
  </section>

</main>
</body>
</html>
```